Brackenfield Security Store Signage with provided LOGO

Need 2 designs (1) indicating the store is around the corner horizontal format and (1) in a vertical format without the around the corner indication. HD image for a 24" by 60" sign. Use attached image for inspiration. Our business of on the south side of a large building and we need to have 2 signs on the front of the build indicating LEFT and the last sign will be a sidewalk sign next to our business.
Updates

Project Deadline Extended
Reason: Allow a couple more designer to sumbit

Industry/Entity Type

Security

Font styles to use
Serif

Colors
33a6d7

Requirements
Must have
• WEBSITE URL: www.vaultwardstation.com and www.brackenfieldsecuritystore.com they can be in small font.
Nice to have
• Phone Number (855) 316-2984

```html
<!DOCTYPE html>
<html lang="en">
<head>
<meta charset="utf-8">
<title>Brackenfield Security Store – Directional Signage</title>
<link href="https://fonts.googleapis.com/css2?family=Oswald:wght@500;700&display=swap" rel="stylesheet">
<style>
  :root {
    --backdrop: #b9b9b9;
    --sign-white: #ffffff;
    --sky: #a8daf0;
    --brand-blue: #33a6d7;
    --deep-blue: #0a6fc0;
    --navy: #0b4f9c;
    --ink: #2a2a2a;
  }
  html, body {
    margin: 0;
    padding: 0;
    width: 1200px;
    height: 1078px;
    overflow: hidden;
    background: var(--backdrop);
  }
  .signage-board {
    display: block;
    width: 1200px;
    height: 1078px;
    font-family: "Oswald", "Arial Narrow", sans-serif;
  }
  .sign-outline { fill: var(--sign-white); filter: url(#drop); }
  .panel-top { fill: url(#skyFade); }
  .panel-arrow { fill: var(--sky); }
  .chevron-band { fill: var(--deep-blue); }
  .chevron-light { fill: var(--brand-blue); }
  .contact-strip { fill: var(--deep-blue); }
  .contact-strip-text { fill: var(--sign-white); font-weight: 500; font-size: 18px; }
  .headline { fill: url(#headlineFill); font-weight: 700; }
  .subline { fill: var(--deep-blue); font-weight: 700; }
  .contact-dark { fill: var(--ink); font-weight: 500; }
  .brand-mark-text { fill: var(--navy); font-weight: 700; font-size: 34px; }
  .brand-mark-dot { fill: var(--navy); }
</style>
</head>
<body>
<svg class="signage-board" viewBox="0 0 1200 1078" xmlns="http://www.w3.org/2000/svg">
  <defs>
    <linearGradient id="skyFade" x1="0" y1="0" x2="0" y2="1">
      <stop offset="0" stop-color="#9fd8f1"/>
      <stop offset="1" stop-color="#f2f9fe"/>
    </linearGradient>
    <linearGradient id="headlineFill" x1="0" y1="0" x2="0" y2="1">
      <stop offset="0" stop-color="#1e90d8"/>
      <stop offset="1" stop-color="#0b4f9c"/>
    </linearGradient>
    <filter id="drop" x="-5%" y="-5%" width="110%" height="115%">
      <feDropShadow dx="4" dy="6" stdDeviation="5" flood-color="#000" flood-opacity="0.35"/>
    </filter>
  </defs>

  <!-- Around-the-corner sign (horizontal) -->
  <g class="sign sign-corner">
    <polygon class="sign-outline" points="212,78 1054,78 1054,456 212,456 114,264"/>
    <polygon class="panel-top" points="216,82 1050,82 1050,452 216,452 120,264"/>
    <polygon class="chevron-band" points="232,94 304,94 200,264 304,438 232,438 138,264"/>
    <polygon class="chevron-light" points="304,94 200,264 214,270 318,94"/>
    <rect class="contact-strip" x="307" y="406" width="747" height="32"/>
    <text class="contact-strip-text" x="335" y="429" textLength="697" lengthAdjust="spacingAndGlyphs">Phone (855) 316-2984  •  www.vaultwardstation.com  •  www.brackenfieldsecuritystore.com</text>

    <g class="brand-mark" role="img" aria-label="Brackenfield Security Store brand mark">
      <circle class="brand-mark-dot" cx="330" cy="256" r="12"/>
      <text class="brand-mark-text" x="350" y="268" textLength="176" lengthAdjust="spacingAndGlyphs">Brackenfield</text>
    </g>

    <text class="headline" x="560" y="268" font-size="118" textLength="448" lengthAdjust="spacingAndGlyphs">BRACKENFIELD</text>
    <text class="subline" x="576" y="352" font-size="76" textLength="420" lengthAdjust="spacingAndGlyphs">SECURITY STORE</text>
  </g>

  <!-- Arrow sign (left) -->
  <g class="sign sign-arrow">
    <polygon class="sign-outline" points="80,774 216,538 244,538 244,584 904,584 952,552 1076,552 1002,772 1076,986 952,986 904,952 244,952 244,1004 216,1004"/>
    <polygon class="panel-arrow" points="90,774 220,546 238,546 238,592 906,592 954,560 1066,560 1012,772 1066,978 954,978 906,944 238,944 238,996 220,996"/>
    <polygon class="chevron-band" points="220,576 112,774 220,976 222,966 126,774 222,588"/>
    <polygon class="chevron-band" points="1040,574 1050,574 1000,772 1050,970 1040,970 990,772"/>

    <text class="contact-dark" x="470" y="625" font-size="27">Phone (855) 316-2984</text>

    <g class="brand-mark" role="img" aria-label="Brackenfield Security Store brand mark">
      <circle class="brand-mark-dot" cx="222" cy="760" r="12"/>
      <text class="brand-mark-text" x="242" y="772" textLength="192" lengthAdjust="spacingAndGlyphs">Brackenfield</text>
    </g>

    <text class="headline" x="472" y="760" font-size="126" textLength="484" lengthAdjust="spacingAndGlyphs">BRACKENFIELD</text>
    <text class="subline" x="490" y="864" font-size="80" textLength="454" lengthAdjust="spacingAndGlyphs">SECURITY STORE</text>

    <text class="contact-dark" x="256" y="938" font-size="25" textLength="638" lengthAdjust="spacingAndGlyphs">www.vaultwardstation.com  •  www.brackenfieldsecuritystore.com</text>
  </g>
</svg>
</body>
</html>
```